YARD FRONTS "N" MORE

catyering to driveway/patio floor construction and remodeling. Concrete, concrete pavers, asphalt, Landscaping, irrigation, pergolas and pools.

Target Market(s)

the home owner that wants to enhance their home

Industry/Entity Type

construction

Contact Information for Business Card

presidet: tomas bellweather email: yardfrontsnmore@example.come office/cell: 555 214 8830

Font styles to use
Sans Serif

Requirements
Must have
• logo should pop out
Nice to have
• the logo should demonstrate that we do exteriors only

```html
<!DOCTYPE html>
<html lang="en">
<head>
<meta charset="utf-8">
<title>Yard Fronts "N" More – Business Cards</title>
<link rel="stylesheet" href="https://fonts.googleapis.com/css2?family=Lato:wght@400;900&family=Nunito:wght@400;800&display=swap">
<style>
  :root {
    --board: #8f8f8f;
    --paper: #ffffff;
    --blue: #178ab9;
    --gold: #d18f07;
    --ink: #2b2b2b;
  }
  * { margin: 0; padding: 0; box-sizing: border-box; }
  html, body { width: 1200px; height: 780px; overflow: hidden; }
  body { background: var(--board); position: relative; font-family: "Lato", sans-serif; }

  .card {
    position: absolute;
    width: 456px;
    height: 261px;
    border-radius: 20px;
    box-shadow: 0 2px 6px rgba(0,0,0,.28);
    overflow: hidden;
  }
  .card--front { background: var(--paper); top: 95px; }
  .card--back { top: 426px; height: 262px; }
  .card--left { left: 125px; }
  .card--right { left: 627px; }
  .card--blue { background: var(--blue); }
  .card--gold { background: var(--gold); }

  .wordmark {
    position: absolute;
    font-family: "Lato", sans-serif;
    font-weight: 900;
    line-height: .95;
    letter-spacing: -.5px;
  }
  .card--front .wordmark {
    left: 36px; top: 104px;
    color: var(--blue);
    font-size: 27px;
  }
  .card--back .wordmark {
    left: 0; right: 0; top: 78px;
    text-align: center;
    color: var(--paper);
    font-size: 46px;
  }
  .wordmark__line { display: block; }

  .contact { position: absolute; left: 244px; top: 66px; width: 196px; }
  .contact__name {
    font-family: "Nunito", sans-serif;
    font-weight: 800;
    font-size: 16.5px;
    color: var(--blue);
    letter-spacing: 0;
    line-height: 1.15;
    white-space: nowrap;
  }
  .contact__title {
    font-family: "Nunito", sans-serif;
    font-size: 13px;
    color: var(--gold);
    margin-top: 3px;
  }
  .contact__rule {
    width: 33px; height: 2px;
    background: var(--blue);
    margin: 7px 0 10px;
  }
  .contact__row {
    display: flex;
    align-items: flex-start;
    gap: 6px;
    color: var(--ink);
    font-size: 11px;
    line-height: 16px;
    letter-spacing: .3px;
    white-space: nowrap;
  }
  .contact__row svg { flex: none; width: 11px; height: 11px; margin-top: 2px; fill: var(--gold); }
  .contact__row--phone { font-size: 14.5px; line-height: 20px; margin-top: 2px; }
  .contact__row--phone svg { margin-top: 4px; }
  .contact__text { padding-left: 1px; }
</style>
</head>
<body>

  <section class="card card--front card--left">
    <div class="wordmark"><span class="wordmark__line">YARD FRONTS</span><span class="wordmark__line">"N" MORE</span></div>
    <div class="contact">
      <h1 class="contact__name">TOMAS BELLWEATHER</h1>
      <p class="contact__title">Presidet</p>
      <div class="contact__rule"></div>
      <div class="contact__row">
        <svg viewBox="0 0 12 12"><path d="M6 0a4 4 0 0 0-4 4c0 3 4 8 4 8s4-5 4-8a4 4 0 0 0-4-4zm0 5.6A1.6 1.6 0 1 1 6 2.4a1.6 1.6 0 0 1 0 3.2z"/></svg>
        <span class="contact__text">880 Linden Crest Rd<br>#12 Marlow, Fla. 30481-1107</span>
      </div>
      <div class="contact__row contact__row--phone">
        <svg viewBox="0 0 12 12"><path d="M2.5 0.8l2 2-1 1.4c.7 1.6 2 2.9 3.6 3.6l1.4-1 2 2-1.3 1.6C5.6 10.3 1.7 6.4 1.1 2.1z"/></svg>
        <span class="contact__text">555 214 8830</span>
      </div>
      <div class="contact__row">
        <svg viewBox="0 0 12 12"><path d="M0 2h12v8H0zm1 1v.4l5 3.3 5-3.3V3zm0 1.6V9h10V4.6L6 7.9z"/></svg>
        <span class="contact__text">yardfrontsnmore@example.com</span>
      </div>
    </div>
  </section>

  <section class="card card--front card--right">
    <div class="wordmark"><span class="wordmark__line">YARD FRONTS</span><span class="wordmark__line">"N" MORE</span></div>
    <div class="contact">
      <h1 class="contact__name">DARIO WHITFIELD</h1>
      <p class="contact__title">Director of Operations</p>
      <div class="contact__rule"></div>
      <div class="contact__row">
        <svg viewBox="0 0 12 12"><path d="M6 0a4 4 0 0 0-4 4c0 3 4 8 4 8s4-5 4-8a4 4 0 0 0-4-4zm0 5.6A1.6 1.6 0 1 1 6 2.4a1.6 1.6 0 0 1 0 3.2z"/></svg>
        <span class="contact__text">880 Linden Crest Rd<br>#12 Marlow, Fla. 30481-1107</span>
      </div>
      <div class="contact__row contact__row--phone">
        <svg viewBox="0 0 12 12"><path d="M2.5 0.8l2 2-1 1.4c.7 1.6 2 2.9 3.6 3.6l1.4-1 2 2-1.3 1.6C5.6 10.3 1.7 6.4 1.1 2.1z"/></svg>
        <span class="contact__text">555 214 8830</span>
      </div>
      <div class="contact__row">
        <svg viewBox="0 0 12 12"><path d="M0 2h12v8H0zm1 1v.4l5 3.3 5-3.3V3zm0 1.6V9h10V4.6L6 7.9z"/></svg>
        <span class="contact__text">yardfrontsnmore@example.com</span>
      </div>
    </div>
  </section>

  <section class="card card--back card--left card--blue">
    <div class="wordmark"><span class="wordmark__line">YARD FRONTS</span><span class="wordmark__line">"N" MORE</span></div>
  </section>

  <section class="card card--back card--right card--gold">
    <div class="wordmark"><span class="wordmark__line">YARD FRONTS</span><span class="wordmark__line">"N" MORE</span></div>
  </section>

</body>
</html>
```